Business Card for a Wellness and Aesthetic Center

I'd like to have a business card design for a Wellness and Aesthetic Center based in the Philippines called "Silvermoss Wellness and Aesthetic Inc." They provide services such as medical and aesthetic dermatology. Specializing on cosmetic and anti-aging procedures.

The target market of the business is mostly women from the upper class from 30 to 60 years old.

The feel and look of the card should be feminine, modern, minimalist and classy.

The colors to play with are gold and black.

The front part should contain:
- Name (example: Marisol Teravid Pangilan, MD)
- Designation (example: Medical Director)
- Company Logo

The back part should contain:
- Company Logo
- Address
- Contact Details
- Website

For more details and inspiration you may visit their website at http://silvermossph.com/

Thank you very much!

Target Market(s)

Women from the upper class from 30 to 60 years old.

Industry/Entity Type

Business

Contact Information for Business Card

- Company Logo

- Company Logo
- Address
- Contact Details
- Website

Font styles to use
Serif
Script

Colors
ffc214
fece3e
faa54b
f78f20
000000

Requirements
Must have
• Design should be feminine, modern, minimalist/simple and classy.
Nice to have
• You can play with lines, curves, gardient and be creative on the placement of texts and logo.
Should not have
• Pictures like body, face or nature scene.

```html
<!DOCTYPE html>
<html lang="en">
<head>
<meta charset="utf-8">
<title>Silvermoss Wellness and Aesthetic Inc. — Business Card</title>
<link rel="stylesheet" href="https://fonts.googleapis.com/css2?family=Open+Sans:wght@300;400;600&display=swap">
<style>
  :root {
    --page-bg: #e9ecee;
    --card-black: #000000;
    --gold-deep: #f78f20;
    --gold-orange: #faa54b;
    --gold-bright: #ffc214;
    --gold-soft: #fece3e;
    --text-light: #e6e6e6;
    --edge-white: #ffffff;
  }
  * { box-sizing: border-box; margin: 0; padding: 0; }
  html, body {
    width: 1200px; height: 900px; overflow: hidden;
    background: var(--page-bg);
    font-family: "Open Sans", sans-serif;
  }
  .sheet {
    width: 1200px; height: 900px;
    display: flex; flex-direction: column; align-items: center; justify-content: center;
    gap: 40px;
  }
  .card {
    position: relative;
    width: 700px; height: 400px;
    background: var(--card-black);
    overflow: hidden;
    box-shadow: 0 10px 28px rgba(0,0,0,0.18);
  }
  .card__swoosh { position: absolute; inset: 0; width: 100%; height: 100%; }
  .brand {
    position: absolute;
    display: flex; align-items: center; gap: 12px;
    color: var(--gold-orange);
    font-weight: 400; font-size: 30px; letter-spacing: 1px;
  }
  .brand__dot {
    width: 14px; height: 14px; border-radius: 50%;
    background: var(--gold-orange);
  }
  .card--front .brand { left: 60px; top: 170px; }
  .holder {
    position: absolute; right: 190px; top: 92px; text-align: right;
  }
  .holder__name {
    color: var(--text-light); font-weight: 300; font-size: 27px; letter-spacing: 0.5px;
  }
  .holder__title {
    margin-top: 6px; color: var(--gold-bright); font-weight: 600; font-size: 14px; letter-spacing: 0.5px;
  }
  .card--back .brand { left: 70px; top: 188px; }
  .divider {
    position: absolute; left: 298px; top: 100px; width: 1px; height: 160px;
    background: linear-gradient(to bottom, transparent, var(--gold-orange), transparent);
    transform: rotate(-22deg);
  }
  .contact {
    position: absolute; left: 360px; top: 58px;
    list-style: none; color: var(--text-light); font-size: 13.5px; font-weight: 400; line-height: 1.45;
  }
  .contact__item { display: flex; align-items: flex-start; gap: 14px; margin-bottom: 12px; }
  .contact__icon { width: 14px; height: 14px; flex: none; margin-top: 3px; fill: var(--gold-bright); }
</style>
</head>
<body>
<main class="sheet">

  <section class="card card--front" aria-label="Business card front">
    <svg class="card__swoosh" viewBox="0 0 700 400" preserveAspectRatio="none" aria-hidden="true">
      <defs>
        <linearGradient id="swooshFront" x1="0" y1="1" x2="1" y2="0">
          <stop offset="0" stop-color="#f78f20"/>
          <stop offset="0.5" stop-color="#faa54b"/>
          <stop offset="1" stop-color="#ffc214"/>
        </linearGradient>
      </defs>
      <path d="M 110 400 C 330 385, 470 250, 700 120 L 700 400 Z" fill="#ffffff"/>
      <path d="M 150 400 C 350 390, 490 262, 700 132 L 700 400 Z" fill="url(#swooshFront)"/>
      <path d="M 300 400 C 450 380, 560 300, 700 250 L 700 400 Z" fill="#f78f20" opacity="0.35"/>
    </svg>
    <div class="brand"><span class="brand__dot"></span><span class="brand__name">Silvermoss</span></div>
    <div class="holder">
      <p class="holder__name">Marisol Teravid Pangilan, MD</p>
      <p class="holder__title">Medical Director</p>
    </div>
  </section>

  <section class="card card--back" aria-label="Business card back">
    <svg class="card__swoosh" viewBox="0 0 700 400" preserveAspectRatio="none" aria-hidden="true">
      <defs>
        <linearGradient id="swooshBack" x1="0" y1="1" x2="1" y2="0">
          <stop offset="0" stop-color="#f78f20"/>
          <stop offset="0.5" stop-color="#faa54b"/>
          <stop offset="1" stop-color="#ffc214"/>
        </linearGradient>
      </defs>
      <path d="M 180 400 C 380 380, 500 260, 700 170 L 700 400 Z" fill="#ffffff"/>
      <path d="M 220 400 C 400 388, 520 272, 700 182 L 700 400 Z" fill="url(#swooshBack)"/>
      <path d="M 380 400 C 500 380, 590 320, 700 290 L 700 400 Z" fill="#f78f20" opacity="0.35"/>
    </svg>
    <div class="brand"><span class="brand__dot"></span><span class="brand__name">Silvermoss</span></div>
    <div class="divider"></div>
    <ul class="contact">
      <li class="contact__item">
        <svg class="contact__icon" viewBox="0 0 16 16" aria-hidden="true"><path d="M8 1 1 7.5h2V15h4v-4h2v4h4V7.5h2Z"/></svg>
        <span>Basement, Linden Crest Tower<br>Harrow Business Park<br>Alabang, Muntinlupa City, PH</span>
      </li>
      <li class="contact__item">
        <svg class="contact__icon" viewBox="0 0 16 16" aria-hidden="true"><path d="M3.6 1.5 6 4 4.8 5.8a9 9 0 0 0 5.4 5.4L12 10l2.5 2.4-1.6 2.1C7.5 14.4 1.6 8.5 1.5 3.1Z"/></svg>
        <span>(632) 555-0148</span>
      </li>
      <li class="contact__item">
        <svg class="contact__icon" viewBox="0 0 16 16" aria-hidden="true"><path d="M1 3.5h14v9H1Zm1.5 1 5.5 4 5.5-4v-.01H2.5Z"/></svg>
        <span>beauty@silvermossph.com</span>
      </li>
      <li class="contact__item">
        <svg class="contact__icon" viewBox="0 0 16 16" aria-hidden="true"><path d="M8 1a7 7 0 1 0 0 14A7 7 0 0 0 8 1Zm0 1.5c.8 0 1.7 1.6 2 4H6c.3-2.4 1.2-4 2-4Zm-5.4 4h2C4.7 5 5 3.8 5.5 3a5.5 5.5 0 0 0-2.9 3.5Zm8.8 0h2A5.5 5.5 0 0 0 10.5 3c.5.8.8 2 .9 3.5ZM2.6 9.5A5.5 5.5 0 0 0 5.5 13c-.5-.8-.8-2-.9-3.5Zm3.4 0c.3 2.4 1.2 4 2 4s1.7-1.6 2-4Zm5.4 0c-.1 1.5-.4 2.7-.9 3.5a5.5 5.5 0 0 0 2.9-3.5Z"/></svg>
        <span>www.silvermossph.com</span>
      </li>
    </ul>
  </section>

</main>
</body>
</html>
```